Lowell Brandt

20 Year Licensed Master Barber specializing in:
men/women cuts, Grooming, Straight razor Shaving and tape line enhancement, beard grooming, eye brow enhancement, South of France, Hot Towel Treatments, Scalp, Blow outs, Shags, Custom Design,RazorCuts,Shear Cuts, Bobs, Perms, Relaxers, Shoe Shine.
Please create a wonderful business card incorporating all the info above and selecting one of the photos. Please be creative.

Barber

```html
<!DOCTYPE html>
<html lang="en">
<head>
<meta charset="utf-8">
<title>Lowell Brandt — Master Barber Business Card</title>
<link rel="stylesheet" href="https://fonts.googleapis.com/css2?family=Courier+Prime&family=Yellowtail&display=swap">
<style>
  :root {
    --stage: #d8d3ca;
    --card: #0a0a0a;
    --ink: #f2f2f2;
    --ink-soft: #cfcfcf;
    --rule: #e6e6e6;
    --art-grey: #5d6670;
    --art-blue: #2e3f5e;
    --art-red: #8a2a36;
  }
  * { box-sizing: border-box; margin: 0; padding: 0; }
  html, body { width: 1200px; height: 1200px; overflow: hidden; }
  body {
    background: var(--stage);
    position: relative;
    font-family: "Courier Prime", "Courier New", monospace;
    color: var(--ink);
  }
  .card {
    position: absolute;
    top: 215px;
    width: 440px;
    height: 770px;
    background: var(--card);
    box-shadow: 0 10px 30px rgba(0,0,0,.35);
  }
  .card--services { left: 130px; }
  .card--identity { left: 630px; }

  /* Services side */
  .services-frame {
    position: absolute;
    inset: 14px;
    border: 2px solid var(--rule);
    display: flex;
    flex-direction: column;
    align-items: center;
    padding: 44px 20px 30px;
  }
  .services-headline {
    font-family: "Yellowtail", cursive;
    font-size: 33px;
    line-height: 1.15;
    text-align: center;
    font-weight: 400;
  }
  .services-divider { margin: 22px 0 24px; }
  .services-list {
    list-style: none;
    text-align: center;
    font-size: 21px;
    line-height: 1.3;
    color: var(--ink-soft);
  }

  /* Identity side */
  .portrait-art {
    position: absolute;
    top: 40px;
    left: 30px;
    width: 380px;
    height: 330px;
    background:
      radial-gradient(ellipse 40% 45% at 50% 55%, var(--art-grey) 0%, transparent 70%),
      radial-gradient(ellipse 30% 35% at 20% 25%, #8c949c 0%, transparent 70%),
      radial-gradient(ellipse 22% 30% at 85% 35%, var(--art-red) 0%, transparent 70%),
      radial-gradient(ellipse 35% 30% at 80% 60%, var(--art-blue) 0%, transparent 75%),
      linear-gradient(to bottom, #202328 0%, var(--card) 100%);
    -webkit-mask-image: radial-gradient(ellipse 70% 65% at 50% 45%, #000 55%, transparent 100%);
            mask-image: radial-gradient(ellipse 70% 65% at 50% 45%, #000 55%, transparent 100%);
  }
  .identity-name {
    position: absolute;
    top: 400px;
    left: 0;
    width: 100%;
    text-align: center;
    font-family: "Yellowtail", cursive;
    font-weight: 400;
    font-size: 66px;
  }
  .identity-contact {
    position: absolute;
    top: 520px;
    left: 52px;
    right: 20px;
    font-size: 21px;
    letter-spacing: 1px;
    line-height: 1.55;
  }
  .contact-line { display: flex; align-items: center; gap: 14px; }
  .contact-line--phone { padding-left: 40px; }
  .social-dot {
    width: 26px; height: 26px; border-radius: 50%;
    background: #3a3a3a;
    flex: none;
  }
  .contact-line--social { margin-top: 6px; }
</style>
</head>
<body>

  <section class="card card--services" aria-label="Services side">
    <div class="services-frame">
      <h2 class="services-headline">20 Year<br>Licensed Master Barber<br>specializing in:</h2>
      <svg class="services-divider" width="300" height="6" viewBox="0 0 300 6" aria-hidden="true">
        <path d="M0 3 Q150 0 300 3 Q150 6 0 3 Z" fill="var(--rule)"/>
      </svg>
      <ul class="services-list">
        <li>men/women cuts</li>
        <li>Grooming</li>
        <li>Straight razor Shaving</li>
        <li>and tape line enhancement</li>
        <li>beard grooming</li>
        <li>eye brow enhancement</li>
        <li>South of France</li>
        <li>Hot Towel Treatments</li>
        <li>Scalp</li>
        <li>Blow outs</li>
        <li>Shags</li>
        <li>Custom Design</li>
        <li>RazorCuts</li>
        <li>Shear Cuts</li>
        <li>Bobs</li>
        <li>Perms</li>
        <li>Relaxers</li>
        <li>Shoe Shine</li>
      </ul>
    </div>
  </section>

  <section class="card card--identity" aria-label="Identity side">
    <div class="portrait-art" role="img" aria-label="Painted portrait collage of the barber with a barber pole, in smoky grey, blue and red tones"></div>
    <h1 class="identity-name">Lowell Brandt</h1>
    <div class="identity-contact">
      <p class="contact-line contact-line--phone">(555)018-2204</p>
      <p class="contact-line">lowell.brandt7@mailbox.com</p>
      <p class="contact-line contact-line--social"><span class="social-dot" aria-hidden="true"></span>lbrandtcuts</p>
      <p class="contact-line contact-line--social"><span class="social-dot" aria-hidden="true"></span>lbrandtcuts</p>
    </div>
  </section>

</body>
</html>
```